Banner for Vet Hospital 5m x 1.2m - Heat Stroke

Meadowlark Pet Hospital needs a Heat Stroke Banner for Summer.
The banner will be 5000mm long and 1200mm tall.

Our region has been hot this year and this summer is going to be extremely hot.
I want to warn people about heat stroke.
I want you to create a heat stroke banner that conveys the symptoms of heat stroke.

Pictures are better than words.
There should be IMAGES and WORDS that can be seen from the road 30m away and maybe some smaller words for people to read as they walk past.

Here are some of the signs of Heat Stroke:
- Panting which increases as heatstroke progresses
- Drooling, salivating
- Agitation, restlessness
- Very red or pale gums
- Bright red tongue
- Increased heart rate
- Breathing distress
- Vomiting Diarrhea (possibly with blood)
- Signs of mental confusion, delirium
- Dizziness, staggering
- Lethargy, weakness
- Muscle tremors
- Seizures
- Collapsing and lying down
- Little to no urine production
- Coma

I have attached characters that we often use in our advertising. They are optional.
I have done a mock up of the design I imagine. You could refine this design or make your own....or both.

Target Market(s)

Women aged 20 to 50.

Industry/Entity Type

Veterinary

Font styles to use
Sans Serif

Colors
fbed22
f78f20
ec1f27
ffffff

Requirements
Must have
• Heat Stroke Symtpms.
• Heat Stroke Warning.
• Summer theme.
Nice to have
• Bright colours.

```html
<!DOCTYPE html>
<html lang="en">
<head>
<meta charset="utf-8">
<title>Heat Stroke Warning Banner</title>
<link rel="stylesheet" href="https://fonts.googleapis.com/css2?family=Bungee&family=Open+Sans:wght@800&display=swap">
<style>
  :root {
    --sun-yellow: #fbed22;
    --heat-orange: #f78f20;
    --alert-red: #ec1f27;
    --white: #ffffff;
    --ink: #111111;
    --glow: #ffd24a;
    --ember: #c74a08;
    --figure-tone: #e8862a;
    --figure-shade: #7a3a0c;
  }
  html, body {
    margin: 0;
    padding: 0;
    overflow: hidden;
  }
  body {
    width: 1200px;
    height: 288px;
    background: var(--white);
  }
  .banner {
    position: relative;
    width: 1200px;
    height: 288px;
    overflow: hidden;
    background:
      radial-gradient(ellipse 55% 95% at 42% 58%, var(--glow) 0%, var(--heat-orange) 45%, var(--ember) 100%);
    font-family: "Open Sans", Arial, sans-serif;
    font-weight: 800;
  }
  .title {
    position: absolute;
    left: 0;
    right: 0;
    top: 4px;
    margin: 0;
    text-align: center;
    padding-left: 60px;
    font-family: "Bungee", "Arial Black", sans-serif;
    font-weight: 400;
    font-size: 50px;
    letter-spacing: 4px;
    word-spacing: 18px;
    color: #f05a22;
    -webkit-text-stroke: 2px var(--white);
    text-shadow: 0 0 3px rgba(0,0,0,0.35);
  }
  .figure {
    position: absolute;
    background: linear-gradient(160deg, var(--figure-tone) 0%, var(--figure-shade) 100%);
    opacity: 0.9;
  }
  .figure--standing { left: 72px; top: 72px; width: 142px; height: 192px; border-radius: 40px 40px 16px 16px; }
  .figure--resting { left: 486px; top: 128px; width: 272px; height: 150px; border-radius: 60px 60px 12px 12px; }
  .figure--collapsed { left: 872px; top: 140px; width: 320px; height: 120px; border-radius: 50px; }

  .symptom {
    position: absolute;
    margin: 0;
    white-space: nowrap;
    text-transform: uppercase;
    line-height: 1;
  }
  .symptom--light { color: var(--white); }
  .symptom--dark { color: var(--ink); }
  .agitation { left: 16px; top: 53px; font-size: 16px; }
  .panting { left: 165px; top: 42px; font-size: 16px; }
  .drooling { left: 213px; top: 117px; font-size: 16px; }
  .breathing { left: 285px; top: 174px; font-size: 16px; }
  .diarrhea { left: 330px; top: 247px; font-size: 25px; }
  .coma { left: 820px; top: 175px; font-size: 24px; }
  .vomiting { left: 740px; top: 256px; font-size: 20px; }
  .tremors { left: 806px; top: 98px; font-size: 20px; }
  .collapse { left: 1066px; top: 96px; font-size: 23px; }

  .arrow { position: absolute; }
  .arrow--first { left: 215px; top: 163px; }
  .arrow--second { left: 752px; top: 162px; }

  .thought {
    position: absolute;
    left: 655px;
    top: 76px;
  }
  .thought__text {
    position: absolute;
    left: 0;
    top: 21px;
    width: 118px;
    text-align: center;
    font-size: 13px;
    color: var(--ink);
    margin: 0;
  }
</style>
</head>
<body>
<main class="banner">
  <h1 class="title">HEAT STROKE</h1>

  <div class="figure figure--standing" role="img" aria-label="Illustrated bulldog standing and panting with tongue out"></div>
  <div class="figure figure--resting" role="img" aria-label="Illustrated bulldog lying down, looking confused"></div>
  <div class="figure figure--collapsed" role="img" aria-label="Illustrated bulldog collapsed on its side"></div>

  <p class="symptom symptom--light agitation">Agitation</p>
  <p class="symptom symptom--light panting">Excessive Panting</p>
  <p class="symptom symptom--light drooling">Drooling</p>
  <p class="symptom symptom--dark breathing">Breathing Distress</p>
  <p class="symptom symptom--dark diarrhea">Diarrhea</p>
  <p class="symptom symptom--dark coma">Coma</p>
  <p class="symptom symptom--dark vomiting">Vomiting</p>
  <p class="symptom symptom--light tremors">Muscles Tremors</p>
  <p class="symptom symptom--light collapse">Collapse</p>

  <svg class="arrow arrow--first" width="52" height="38" viewBox="0 0 52 38" aria-hidden="true">
    <polygon points="0,0 52,19 0,38 10,19" fill="#f05a22"/>
  </svg>
  <svg class="arrow arrow--second" width="48" height="34" viewBox="0 0 48 34" aria-hidden="true">
    <polygon points="0,0 48,17 0,34 9,17" fill="#f05a22"/>
  </svg>

  <div class="thought">
    <svg width="120" height="85" viewBox="0 0 120 85" aria-hidden="true">
      <path d="M20 12 Q30 0 45 8 Q58 -2 72 7 Q88 0 98 12 Q116 14 112 32 Q120 46 104 54 Q100 66 84 62 Q72 72 58 63 Q44 70 34 62 Q16 66 14 52 Q0 46 8 32 Q2 16 20 12 Z M72 62 L80 84 L86 60 Z"
            fill="#ffffff" stroke="#111111" stroke-width="2" stroke-linejoin="round"/>
    </svg>
    <p class="thought__text">CONFUSION</p>
  </div>
</main>
</body>
</html>
```